uk based ecommerce website requires fresh look ,high quality look and feel

we are a web based company selling eco friendly ground reinforcement grids to diy and construction sectors
our existing website is www.plumbrooksurfacing.co.uk ,

we have already updated the logo so that is the branding sorted .so we need a ecommerce website that is very much up-to date in design and layout and which has content management system for ease of use so that we can add products and information as required.

Use current logo as reference for colour scheme.
www.plumbrooksurfacing.co.uk

The current website has 6 pages accessible through the navigation bar, I would now like 5 pages, removing the need for the Trade Enquiries page possibly have it with along with contact us.
Updates

Target Market(s)

construction industry , diy end users,
retail market, landscapers, gardeners

Industry/Entity Type

Construction

Font styles to use
Other font styles liked:
• logo font prometo

Colors
f78f20
9bcb3c

Requirements
Must have
• logo colours and logo design in website with cms responsive design for tablet and mobile devices
• expect content to work flawlessly and look great across all devices
• HTML 5 custom design with coding as required
• must have good experiance in ecommerce website design
• eye catching, high quality look and feel and very user friedly ,very up-to date.
Nice to have
• picture slider show
• explain in writing what exactly i am getting in my ecommerce website
Should not have
• plain , basic design , old fashion looking ,cheap look

```html
<!DOCTYPE html>
<html lang="en">
<head>
<meta charset="utf-8">
<title>Ground Solutions – Plumbrook Surfacing</title>
<link href="https://fonts.googleapis.com/css2?family=Open+Sans:wght@400;600;700&family=Raleway:wght@500;600&display=swap" rel="stylesheet">
<style>
:root{
  --orange:#f78f20;
  --green:#8cbf3a;
  --dark:#231f20;
  --footer:#2a2526;
  --text:#5a5a5a;
  --heading:#262626;
  --line:#e3e3e3;
  --white:#ffffff;
}
*{box-sizing:border-box;margin:0;padding:0}
html,body{width:1200px;height:1092px;overflow:hidden;background:var(--white)}
body{font-family:'Open Sans',sans-serif;color:var(--text);position:relative}
.wrap{position:absolute;left:89px;width:1022px}

/* header */
.site-header{position:absolute;top:0;left:0;width:1200px;height:79px}
.brand{left:89px;top:18px;display:flex;align-items:center;gap:8px;position:absolute}
.brand-dot{width:34px;height:34px;border-radius:50%;background:var(--green)}
.brand-name{font-family:'Open Sans',sans-serif;font-weight:700;font-size:15px;color:var(--orange);line-height:1.1;letter-spacing:.3px}
.search{position:absolute;left:399px;top:18px;width:286px;height:42px;border:1px solid #d9d9d9;border-radius:21px;overflow:hidden;display:flex}
.search span{flex:1;font-size:12px;color:#777;padding:12px 18px}
.search-btn{width:46px;background:var(--orange);display:flex;align-items:center;justify-content:center}
.tele{position:absolute;left:762px;top:24px;display:flex;gap:10px}
.tele-label{font-size:14px;color:var(--heading);line-height:1.5}
.tele-label b{font-family:'Raleway',sans-serif;font-weight:600;font-size:17px;letter-spacing:.5px}
.tele-numbers{position:absolute;right:89px;top:15px;text-align:right;font-weight:700;font-size:19px;line-height:23px}
.tele-numbers .o{color:var(--orange)}
.tele-numbers .g{color:var(--green)}

/* nav */
.main-nav{position:absolute;top:79px;left:0;width:1200px;height:47px;background:var(--dark)}
.main-nav ul{list-style:none;display:flex;position:absolute;left:96px;top:0}
.main-nav li{font-size:13.5px;color:var(--white);height:47px;line-height:47px;padding:0 18px}
.main-nav li.active{background:var(--orange)}
.account{position:absolute;right:89px;top:0;height:47px;display:flex;align-items:center;gap:12px;color:var(--white);font-size:13.5px}
.cart{position:relative;width:22px;height:20px}
.cart-badge{position:absolute;top:-10px;right:-10px;width:15px;height:15px;border-radius:50%;background:var(--green);font-size:9px;line-height:15px;text-align:center;color:var(--white)}

/* hero */
.page-hero{position:absolute;top:126px;left:0;width:1200px;height:178px;background:linear-gradient(90deg,#f1f1f1 0%,#e6e6e4 45%,#c9c7c2 65%,#8b8474 75%,#cfcdc8 88%,#bdbbb5 100%)}
.page-title{position:absolute;left:91px;top:63px;font-family:'Raleway',sans-serif;font-weight:500;font-size:37px;color:var(--heading)}
.breadcrumb{position:absolute;left:89px;top:104px;font-size:13px;color:var(--heading);display:flex;align-items:center;gap:7px}

/* content */
.enquiry-card{position:absolute;left:89px;top:355px;width:379px;height:395px;border:1px solid var(--line)}
.card-photo{height:214px;background:linear-gradient(180deg,#2b2d30 0%,#5c5d5f 30%,#9a9a98 60%,#b8b8b6 100%)}
.card-body{padding:20px 20px 0 22px}
.card-body h3{font-weight:400;font-size:16.5px;line-height:25px;color:var(--heading);margin-bottom:10px}
.card-body p{font-size:11.8px;line-height:19.5px;color:#333;margin-left:-2px}
.article{position:absolute;left:513px;top:355px;width:598px}
.article h2{font-family:'Raleway',sans-serif;font-weight:500;font-size:27px;color:var(--heading);border-left:3px solid var(--green);padding:8px 0 4px 19px;margin-bottom:17px;line-height:36px}
.article p{font-size:13.2px;line-height:23px;margin-bottom:10px}

/* footer */
.site-footer{position:absolute;top:806px;left:0;width:1200px;height:238px;background:var(--footer)}
.f-col{position:absolute;top:27px}
.f-col h4{font-weight:400;font-size:15.5px;color:var(--white);padding-bottom:13px;border-bottom:1px solid #4a4445;margin-bottom:18px}
.f-about{left:88px;width:238px}
.f-about p{font-size:12px;line-height:18px;color:var(--white);margin-bottom:4px}
.f-gallery{left:343px;width:237px}
.thumbs{display:grid;grid-template-columns:repeat(3,75px);gap:6px 5px}
.thumbs div{height:57px}
.f-contact{left:598px;width:237px}
.f-contact .addr{font-size:11.8px;line-height:19.5px;color:var(--white);padding-left:7px}
.f-contact .ph{font-weight:700;font-size:15px;line-height:19px;padding-left:7px;margin-top:10px}
.f-follow{left:856px;width:255px}
.social{display:flex;gap:10px;margin-top:-2px}
.social span{width:40px;height:40px;border-radius:50%}
.cards{display:flex;gap:5px;margin-top:24px}
.cards span{width:45px;height:28px;border-radius:2px;background:var(--white)}
.bottom-bar{position:absolute;top:1044px;left:0;width:1200px;height:48px;background:var(--orange);color:var(--white);font-size:12.5px}
.bottom-bar .copy{position:absolute;left:89px;top:16px}
.bottom-bar ul{list-style:none;display:flex;gap:24px;position:absolute;right:89px;top:17px}
</style>
</head>
<body>

<header class="site-header">
  <div class="brand"><span class="brand-dot"></span><span class="brand-name">PLUMBROOK<br>SURFACING</span></div>
  <div class="search"><span>Search</span>
    <div class="search-btn"><svg width="18" height="18" viewBox="0 0 18 18"><circle cx="7.5" cy="7.5" r="5.5" fill="none" stroke="#fff" stroke-width="2"/><line x1="11.5" y1="11.5" x2="16" y2="16" stroke="#fff" stroke-width="2.4" stroke-linecap="round"/></svg></div>
  </div>
  <div class="tele">
    <svg width="34" height="34" viewBox="0 0 24 24"><path fill="#f78f20" d="M6.6 10.8a15.1 15.1 0 0 0 6.6 6.6l2.2-2.2c.3-.3.7-.4 1-.2 1.1.4 2.3.6 3.6.6.6 0 1 .4 1 1V20c0 .6-.4 1-1 1A17 17 0 0 1 3 4c0-.6.4-1 1-1h3.5c.6 0 1 .4 1 1 0 1.3.2 2.5.6 3.6.1.3 0 .7-.2 1z"/></svg>
    <div class="tele-label"><b>TELE</b><br>hour messaging service 24</div>
  </div>
  <div class="tele-numbers"><div class="o">0141-555-0182</div><div class="g">0800-555-0145</div></div>
</header>

<nav class="main-nav">
  <ul>
    <li>Home</li><li>Shop</li><li>About Us</li><li class="active">Ground Solutions</li><li>Plumbrook</li><li>Contact Us</li>
  </ul>
  <div class="account">Login | Register
    <div class="cart"><svg width="22" height="20" viewBox="0 0 22 20"><path d="M1 2h3l2.5 11h11l2.5-8H6" fill="none" stroke="#f78f20" stroke-width="2.2" stroke-linejoin="round"/><circle cx="8" cy="17" r="1.8" fill="#f78f20"/><circle cx="16" cy="17" r="1.8" fill="#f78f20"/></svg><span class="cart-badge">0</span></div>
  </div>
</nav>

<section class="page-hero" role="img" aria-label="Banner photo of a worker laying ground grid on an airfield with aircraft behind">
  <h1 class="page-title">Ground Solutions</h1>
  <div class="breadcrumb">
    <svg width="15" height="13" viewBox="0 0 15 13"><path d="M7.5 0 0 6.5h2V13h4V9h3v4h4V6.5h2z" fill="#262626"/></svg>
    <span>Home</span><span>/</span><span>Ground Solutions</span>
  </div>
</section>

<aside class="enquiry-card">
  <div class="card-photo" role="img" aria-label="Photo of a car wheel on a fresh gravel driveway"></div>
  <div class="card-body">
    <h3>All enquiries by email on our contact page or by Calling on : 0800-555-0145</h3>
    <p>Our If you feel this is the best choice for you then go to our online store and buy with confidence because this is a light-weight eco-friendly and which is easy to handle and so simple to lay system.</p>
  </div>
</aside>

<article class="article">
  <h2>Gravel Driveways</h2>
  <p>Gravel driveways are one of the most popular choices for driveways and hard landscaping in the UK and it's easy to see why. It's cost effective, low maintenance and looks great particularly in rural settings or in town where it matches the predominant stone and brick colouring of the area.</p>
  <p>There is an immense choice of size, colours and shapes available, making it an excellent choice for resurfacing. Gravel is also a very good deterrent against any kind of burglary as it makes a crunching noise as you walk over the surface, making it not a favorite amongst the undesirables of our society.</p>
  <p>The combination of gravel and our Cellular ground reinforcement grid system's makes the perfect choice for the modern driveway or path, Incorporating the tried and tested gravel driveway and combining with the holding chambers of the ground reinforcement system. This will not be moving around like the normal gravel driveway which makes it the perfect choice. This system does not require planning permission as it is free draining allowing water back into the ground &nbsp;replenishing instead of putting strain on our street drainage systems.</p>
</article>

<footer class="site-footer">
  <div class="f-col f-about">
    <h4>About Us</h4>
    <p>Consectetuer adipiscing elit. Aenean commodo ligula eget dolor.</p>
    <p>consectetuer adipiscing elit. Aenean commodo ligula eget dolor. Aenean massa. Cum sociis natoque penatibus et magnis dis parturient montes.</p>
  </div>
  <div class="f-col f-gallery">
    <h4>Gallery</h4>
    <div class="thumbs">
      <div role="img" aria-label="Photo of grids being laid on soil" style="background:linear-gradient(#8a7a66,#5a5048)"></div>
      <div role="img" aria-label="Photo of grass growing through grid" style="background:linear-gradient(#3e4a2c,#6f8a3c)"></div>
      <div role="img" aria-label="Photo of green mesh grid" style="background:linear-gradient(#4f6a3a,#6e8a58)"></div>
      <div role="img" aria-label="Photo of gravel filled grid" style="background:linear-gradient(#7a7a80,#a89c84)"></div>
      <div role="img" aria-label="Photo of garden planting" style="background:linear-gradient(#6e8a3c,#8a7a50)"></div>
      <div role="img" aria-label="Photo of a car on a gravel driveway" style="background:linear-gradient(#8a8e86,#6a6a66)"></div>
    </div>
  </div>
  <div class="f-col f-contact">
    <h4>Contact Info</h4>
    <p class="addr">PLUMBROOK SURFACING LTD<br>Ashdown House, Brookfield Ind Est,<br>Carrowmore, G99 1ZZ</p>
    <p class="ph"><span style="color:var(--green)">0141-555-0182</span><br><span style="color:var(--orange)">0800-555-0145</span></p>
  </div>
  <div class="f-col f-follow">
    <h4>Follow Us</h4>
    <div class="social"><span style="background:#3b5a9a"></span><span style="background:#2aa8e0"></span><span style="background:#d93a30"></span></div>
    <div class="cards"><span></span><span></span><span></span><span></span></div>
  </div>
</footer>

<div class="bottom-bar">
  <span class="copy">© 2016 &nbsp;plumbrook surfacing ltd</span>
  <ul><li>Site Map</li><li>Email Terms of Service</li><li>Delivery and Returns</li></ul>
</div>

</body>
</html>
```